RidgeHornSupply.com

I need a new webdesign for a company in the Ridge Horn/SF Bay area that showcases the financial benefits of buying used band instruments for junior high students.This would be opposed to the current and costly option of renting cheap quality instruments from the 2 or 3 local music stores that charge a monthly fee that over the years charges the buyer 3 or 4x over..
Instruments: focus in on Alto Sax, Trumpet, Flute, Clarinet, Trombone, Tenor Sax, Baritone
Target middle schools are Kestrelwood Middle School and Harlow Middle School in Ridge Horn, CA. Both have award winning band programs.
Files attached may or may not be important.
Tabs Needed and funtional
Contact
Shopping Cart
Select Instrument
Checkout
Add to Cart, etc.
Instuments
quantity, etc.
trade in your instrument/sell your instrument
ability to add or take away new instruments for sale. including pictures
Additional questions or info, feel free to ask
Hi Designers,
Project Deadline Extended
Reason: In the next week you will be receiving specific content that will be required to be had on the website.
New desigins are still welcome. Please continue to contact me if you have questions about your individual designs.
Thanks!
Ridge Horn

```html
<!DOCTYPE html>
<html lang="en">
<head>
<meta charset="utf-8">
<title>Ridge Horn – Band Instruments</title>
<link href="https://fonts.googleapis.com/css2?family=Jost:wght@300;400;500&family=Open+Sans:wght@400;600&display=swap" rel="stylesheet">
<style>
:root{
  --green:#7cb518;
  --green-dark:#5f9410;
  --orange:#f26f11;
  --ink:#333;
  --muted:#666;
  --footer:#1e1e1e;
  --footer-line:#2e2e2e;
  --footer-text:#8c8c8c;
}
*{box-sizing:border-box;margin:0;padding:0}
html,body{width:718px;height:1200px;overflow:hidden;background:#fff}
body{position:relative;font-family:"Open Sans",sans-serif;color:var(--ink)}
.abs{position:absolute}
h1,h2,h3,h4{font-weight:400}
.header{left:0;top:0;width:718px;height:57px;background:linear-gradient(#fff,#f1f1f1)}
.logo{font-family:"Jost",sans-serif;font-weight:400;font-size:17px;letter-spacing:.5px;color:#444;display:flex;align-items:center;gap:5px;white-space:nowrap}
.logo .mark{width:8px;height:8px;border-radius:50%;background:var(--green)}
.search{left:380px;top:20px;width:123px;height:18px;border:1px solid #ccc;border-radius:9px;background:#fff;font-size:7px;color:#999;padding:4px 9px}
.search svg{position:absolute;right:7px;top:4px}
.cart{left:507px;top:20px;width:68px;height:18px;border:1px solid #ccc;border-radius:9px;background:#fff;font-size:7px;color:#999;padding:4px 10px}
.cart b{color:var(--green);margin-left:5px}
.login{left:579px;top:21px;width:57px;height:16px;border-radius:8px;background:var(--orange);color:#fff;font-size:7.5px;text-align:center;line-height:16px}
.nav{left:0;top:57px;width:718px;height:26px;background:var(--green)}
.nav a{position:absolute;top:0;height:26px;line-height:26px;color:#fff;font-size:7.5px;text-decoration:none;transform:translateX(-50%);white-space:nowrap}
.nav a.active{background:var(--orange);width:59px;text-align:center}
.hero{left:0;top:83px;width:718px;height:298px;background:linear-gradient(135deg,#3d4a40,#1f2a24 45%,#2b3329 70%,#151a16)}
.hero-title{left:0;width:718px;top:182px;text-align:center;font-family:"Jost",sans-serif;font-size:37px;color:var(--orange);letter-spacing:1px}
.hero-copy{left:100px;width:518px;top:229px;text-align:center;font-size:11.5px;line-height:16px;color:#fff}
.btn-shop{left:304px;top:274px;width:110px;height:25px;border-radius:13px;background:linear-gradient(#8fcf22,var(--green-dark));color:#fff;font-size:11px;text-align:center;line-height:25px}
.hero-rule{top:287px;width:66px;border-top:1px dotted rgba(255,255,255,.5)}
.arrow{top:217px;width:26px;height:26px;border-radius:50%;background:rgba(0,0,0,.45)}
.arrow svg{position:absolute;left:9px;top:8px}
.dots{left:341px;top:354px;display:flex;gap:3px}
.dots i{width:6px;height:6px;border-radius:50%;background:#fff}
.dots i.on{background:var(--orange)}
.section-title{left:0;width:718px;text-align:center;font-family:"Jost",sans-serif;font-size:27px;color:#333;letter-spacing:.5px}
.section-title span{color:var(--green)}
.title-rule{height:1px;background:#ccc}
.section-copy{text-align:center;color:var(--muted)}
.btn-more{left:314px;top:507px;width:91px;height:23px;border-radius:12px;background:var(--orange);color:#fff;font-size:9.5px;text-align:center;line-height:23px}
.tile{color:#fff}
.tile h3{position:absolute;font-family:"Jost",sans-serif;font-size:15.5px;letter-spacing:.3px}
.tile p{position:absolute;font-size:6.5px;line-height:8.5px;width:100px}
.tile .buy{position:absolute;width:59px;height:15px;border:1px solid rgba(255,255,255,.85);font-size:5.5px;line-height:13px;text-align:center}
.tile.right h3,.tile.right p{right:14px;text-align:right}
.tile.right .buy{right:14px}
.tile.left h3,.tile.left p,.tile.left .buy{left:13px}
.partners{left:0;top:980px;width:718px;height:31px;background:#fff;border-top:1px solid #e2e2e2}
.partners div{position:absolute;top:0;height:31px;width:69px;border-left:1px solid #e2e2e2;text-align:center;line-height:31px;font-family:"Jost",sans-serif;font-weight:500;font-size:10px;color:#666}
.footer{left:0;top:1011px;width:718px;height:189px;background:var(--footer)}
.foot-h{font-family:"Jost",sans-serif;font-size:12px;color:var(--green)}
.foot-list{font-size:7.5px;color:var(--footer-text);line-height:14.5px;list-style:none}
.foot-list li:first-child{color:#fff}
.field{width:127px;height:19px;background:#fff;border-radius:2px;font-size:6.5px;color:#999;padding:5px 8px}
.subscribe{left:178px;top:1134px;width:59px;height:18px;background:var(--orange);color:#fff;font-size:7px;text-align:center;line-height:18px}
.social{font-size:7.5px;color:var(--footer-text);display:flex;align-items:center;gap:9px}
.social i{width:15px;height:15px;border-radius:50%;border:1px solid #666}
.card{top:1120px;width:21px;height:13px;border-radius:1px}
.copyright{left:0;width:718px;top:1178px;text-align:center;font-size:7.5px;color:var(--footer-text)}
</style>
</head>
<body>

<header class="abs header">
  <div class="abs logo" style="left:82px;top:19px"><span>RIDGE</span><span class="mark"></span><span>HORN</span></div>
  <div class="abs search">Search
    <svg width="8" height="8" viewBox="0 0 8 8"><circle cx="3.3" cy="3.3" r="2.4" fill="none" stroke="#7cb518" stroke-width="1.1"/><path d="M5 5l2.4 2.4" stroke="#7cb518" stroke-width="1.2"/></svg>
  </div>
  <div class="abs cart">CART<b>0</b> ▾</div>
  <div class="abs login">LOG IN</div>
</header>

<nav class="abs nav">
  <a class="active" style="left:113px">HOME</a>
  <a style="left:180px">INSTRUMENT</a>
  <a style="left:256px">CHECKOUT</a>
  <a style="left:327px">QUANTITY</a>
  <a style="left:408px">SHOPPING CART</a>
  <a style="left:495px">CONTACT US</a>
  <a style="left:576px">MY ACCOUNT</a>
</nav>

<section class="abs hero" role="img" aria-label="Marching band musician holding a brass instrument, band members behind"></section>
<h1 class="abs hero-title">WELCOME TO RIDGE HORN</h1>
<p class="abs hero-copy">Lorem Ipsum is simply dummy text of typesetting industry. Lorem Ipsum has been the industry's standard dummy text ever since the 1500s. when an unknown.</p>
<div class="abs hero-rule" style="left:236px"></div>
<div class="abs hero-rule" style="left:416px"></div>
<div class="abs btn-shop">🛒 SHOP NOW</div>
<div class="abs arrow" style="left:28px"><svg width="8" height="10"><path d="M6 1L2 5l4 4" fill="none" stroke="#fff" stroke-width="1.5"/></svg></div>
<div class="abs arrow" style="left:663px"><svg width="8" height="10"><path d="M2 1l4 4-4 4" fill="none" stroke="#fff" stroke-width="1.5"/></svg></div>
<div class="abs dots"><i></i><i></i><i class="on"></i><i></i><i></i></div>

<div class="abs title-rule" style="left:222px;top:429px;width:64px"></div>
<div class="abs title-rule" style="left:437px;top:429px;width:64px"></div>
<h2 class="abs section-title" style="top:410px">ABOUT <span>US</span></h2>
<p class="abs section-copy" style="left:86px;width:546px;top:452px;font-size:10.5px;line-height:14.5px">Lorem Ipsum is simply dummy text of typesetting industry. Lorem Ipsum has been. the industry's standard dummy text ever since the 1500s, when an unknown printer took a galley of type and scrambled it to make a type specimen book.  It has survived not only five centuries, but also the leap into electronic.</p>
<div class="abs btn-more">VIEW MORE ⊙</div>

<div class="abs title-rule" style="left:204px;top:578px;width:52px"></div>
<div class="abs title-rule" style="left:509px;top:578px;width:56px"></div>
<h2 class="abs section-title" style="top:559px">OUR <span>INSTRUMENT</span></h2>
<p class="abs section-copy" style="left:108px;width:542px;top:599px;font-size:9px;line-height:13px">Lorem Ipsum is simply dummy text of typesetting industry. Lorem Ipsum has been. the industry's standard dummy text ever since the 1500s, when an unknown printer took a galley of type and scrambled it to make a type specimen book.  It has survived not only five centuries, but also the leap into electronic typesetting.</p>

<div class="abs tile left" style="left:83px;top:658px;width:174px;height:89px;background:linear-gradient(90deg,#3a3a44,#8a8a9a 60%,#c9c9d6)" role="img" aria-label="Alto saxophone in an open case">
  <h3 style="top:12px">ALTO SAX</h3><p style="top:32px">It is a long established fact that a readerbe.</p><div class="buy" style="top:58px">🛒 SHOP NOW</div>
</div>
<div class="abs tile left" style="left:83px;top:758px;width:174px;height:89px;background:linear-gradient(90deg,#3b3b3b,#6b6b6b 60%,#b7a05a)" role="img" aria-label="Brass trumpet on a grey background">
  <h3 style="top:12px">TRUMPET</h3><p style="top:32px">It is a long established fact that a readerbe.</p><div class="buy" style="top:58px">🛒 SHOP NOW</div>
</div>
<div class="abs tile left" style="left:83px;top:858px;width:174px;height:89px;background:linear-gradient(90deg,#1f2a44,#3c5584 60%,#c9d1e0)" role="img" aria-label="Close-up of a silver flute">
  <h3 style="top:12px">FLUTE</h3><p style="top:32px">It is a long established fact that a readerbe.</p><div class="buy" style="top:58px">🛒 SHOP NOW</div>
</div>
<div class="abs tile" style="left:269px;top:658px;width:181px;height:290px;background:linear-gradient(#3b3b3b,#222 60%,#2f2a26)" role="img" aria-label="Row of black clarinets standing upright">
  <h3 style="top:113px;width:181px;text-align:center">CLARINET</h3>
  <p style="top:135px;left:10px;width:161px;text-align:center;font-size:7.5px;line-height:11px">It is a long established fact that a reader will be distracted by the readable content of a page when looking</p>
  <div class="buy" style="top:180px;left:54px;width:76px;height:20px;line-height:18px;font-size:7.5px">🛒 SHOP NOW</div>
</div>
<div class="abs tile right" style="left:462px;top:658px;width:174px;height:89px;background:linear-gradient(90deg,#c8c8c2,#8c8a84 50%,#4a4844)" role="img" aria-label="Trombone lying on a light surface">
  <h3 style="top:12px">TROMBONE</h3><p style="top:32px">It is a long established fact that a readerbe.</p><div class="buy" style="top:58px">🛒 SHOP NOW</div>
</div>
<div class="abs tile right" style="left:462px;top:758px;width:174px;height:89px;background:linear-gradient(90deg,#8a8a80,#5a5648 50%,#2a2a2a)" role="img" aria-label="Tenor saxophone in a case">
  <h3 style="top:12px">TENOR SAX</h3><p style="top:32px">It is a long established fact that a readerbe.</p><div class="buy" style="top:58px">🛒 SHOP NOW</div>
</div>
<div class="abs tile right" style="left:462px;top:859px;width:174px;height:89px;background:linear-gradient(90deg,#a9a9a9,#5f5f5f 50%,#1f1f1f)" role="img" aria-label="Silver baritone horn on a dark background">
  <h3 style="top:12px">TENOR SAX</h3><p style="top:32px">It is a long established fact that a readerbe.</p><div class="buy" style="top:58px">🛒 SHOP NOW</div>
</div>

<div class="abs partners">
  <div style="left:90px">Quadra</div>
  <div style="left:159px">Lensworth</div>
  <div style="left:228px">Chipwell</div>
  <div style="left:297px">Gatehall</div>
  <div style="left:366px">Crispo</div>
  <div style="left:434px">Brightmint</div>
  <div style="left:503px">Cocoro</div>
  <div style="left:572px;border-right:1px solid #e2e2e2">Cocoro</div>
</div>

<footer class="abs footer"></footer>
<h4 class="abs foot-h" style="left:82px;top:1034px">Site Map</h4>
<ul class="abs foot-list" style="left:82px;top:1056px">
  <li>Home</li><li>About us</li><li>Instrument</li><li>Checkout</li><li>Quantity</li><li>Shopping cart</li><li>Contact Us</li>
</ul>
<h4 class="abs foot-h" style="left:178px;top:1034px">Signup to Our Newsletters</h4>
<p class="abs" style="left:178px;top:1058px;width:140px;font-size:6.5px;line-height:9px;color:#aaa">Lorem Ipsum is simply dummy text of the printing and typesetting industry.</p>
<div class="abs field" style="left:178px;top:1086px">Name</div>
<div class="abs field" style="left:178px;top:1109px">Email</div>
<div class="abs subscribe">SUBSCRIBE</div>
<h4 class="abs foot-h" style="left:366px;top:1034px">Follow Us</h4>
<div class="abs social" style="left:366px;top:1059px"><i></i>Chirpline</div>
<div class="abs social" style="left:366px;top:1077px"><i></i>Friendwall</div>
<div class="abs social" style="left:366px;top:1095px"><i></i>Rss</div>
<div class="abs social" style="left:366px;top:1114px"><i></i>Worknet</div>
<div class="abs social" style="left:366px;top:1133px"><i></i>Circleplus</div>
<div class="abs logo" style="left:510px;top:1064px;color:#888;font-size:18px"><span>RIDGE</span><span class="mark"></span><span>HORN</span></div>
<h4 class="abs foot-h" style="left:510px;top:1098px">Payment Option</h4>
<div class="abs card" style="left:511px;background:#f4f4f4"></div>
<div class="abs card" style="left:537px;background:#e0b400"></div>
<div class="abs card" style="left:563px;background:#e9eef5"></div>
<div class="abs card" style="left:589px;background:#c8102e"></div>
<div class="abs card" style="left:615px;background:#2a6fb6"></div>
<div class="abs" style="left:0;top:1170px;width:718px;height:1px;background:var(--footer-line)"></div>
<p class="abs copyright">© 2014 Ridge Horn. All Rights Reserved. Terms &amp; conditions</p>

</body>
</html>
```